Charity website needing new website design

Hi there. We are looking to get a revamped website for our non for profit charity. We specialise in eye cataract surgeries and ear care around the world. Please visit our website brightpathrelief.org.au for the current layout.
I have attached a brief with photos. The about us page please include an interactive map showing our locations we operate in. The website should be easy to use, match our logo design and be clear to navigate. Pixelvault and other images can be used if they fit the scheme of the website and feel. The donation page should incorporate the gateway to receive donations. The team page should have each photo of the team member next to it. Please compare to other charity websites such as KORAMEN, Globe Harbor etc. Another website which has a lovely and easy to use scheme is tlnqaustralia.org.au
The tabs should be in the following order:
About us, Why Health? Our Team, Eye Care Programs, Ear Care Programs, Contact Us, Donate.
Please make sure the website is both compatible with mobile & computer.
The Registered Charity Logo can be at the footer of the page with details of brightpath etc

```html
<!DOCTYPE html>
<html lang="en">
<head>
<meta charset="utf-8">
<title>Brightpath Aid Foundation</title>
<link rel="stylesheet" href="https://fonts.googleapis.com/css2?family=Montserrat:wght@400;500;600;700;800;900&display=swap">
<style>
:root{
  --navy:#0b4862;
  --navy-dark:#093d54;
  --orange:#f0922d;
  --orange-deep:#e07f1c;
  --lime:#a8c03a;
  --lime-deep:#8aa531;
  --green:#3db872;
  --green-deep:#25a15c;
  --grey:#8a8a8a;
  --white:#ffffff;
}
*{margin:0;padding:0;box-sizing:border-box}
html,body{width:1200px;height:3196px;overflow:hidden}
body{position:relative;font-family:"Montserrat",sans-serif;background:var(--white);color:var(--navy)}
.abs{position:absolute}
.btn{position:absolute;display:flex;align-items:center;justify-content:center;background:var(--orange);color:var(--white);font-size:15px;font-weight:500;border-radius:3px;box-shadow:0 4px 8px rgba(0,0,0,.18)}

/* header */
.social{display:flex;gap:14px;align-items:center}
.social span{display:block;width:22px;height:22px;border-radius:50%;border:2px solid var(--navy)}
.social span:first-child{background:var(--orange);border-color:var(--orange);width:30px;height:30px}
.brand{left:452px;top:18px;display:flex;align-items:center;gap:10px}
.brand .mark{width:40px;height:40px;border-radius:50%;background:var(--green)}
.brand .name{font-weight:700;font-size:26px;line-height:1;color:var(--navy);letter-spacing:.5px;white-space:nowrap}
.brand .name small{display:block;font-size:17px;letter-spacing:2px;margin-top:3px}
.nav{left:0;top:80px;width:1200px;height:41px;background:var(--navy);display:flex;align-items:center;padding-left:104px;color:var(--white);font-size:15px}
.nav a{display:block;padding:0 18px;line-height:41px}
.nav a.active{background:var(--green);padding:0 18px}
.nav i{font-style:normal;opacity:.9}

/* hero */
.hero{left:0;top:121px;width:1200px;height:576px;background:linear-gradient(100deg,#d9731f 0%,#c4862b 35%,#a89c35 60%,#7fa63a 100%)}
.hero-copy{left:618px;top:248px;color:var(--white)}
.hero-copy p{font-size:33px;font-weight:500;letter-spacing:2px;line-height:40px;white-space:nowrap}
.hero-copy .hl{display:inline-block;background:var(--green);padding:0 10px 0 8px;margin-left:-8px}
.planet{left:612px;top:358px;font-size:118px;font-weight:800;color:transparent;-webkit-text-stroke:3px var(--white);letter-spacing:4px;line-height:1}
.slides{left:622px;top:628px;display:flex;gap:8px}
.slides span{width:27px;height:3px;background:var(--white)}
.slides span:first-child{background:var(--orange)}

/* donate */
.donate{top:682px;width:326px;height:107px;display:flex;align-items:center;color:var(--white)}
.donate .lbl{position:absolute;left:54px;top:38px;font-size:27px;font-weight:600}
.donate .coin{position:absolute;left:160px;top:-25px;width:106px;height:106px;border-radius:50%;display:flex;flex-direction:column;align-items:center;justify-content:center}
.donate .coin small{font-size:17px;font-weight:600}
.donate .coin b{font-size:46px;font-weight:600;line-height:1}

/* about */
.kicker{font-size:16px;font-weight:600;color:var(--orange)}
.h-big{font-weight:600;line-height:1;color:var(--navy);white-space:nowrap}
.about-copy{left:618px;top:1025px;width:470px;font-size:13px;line-height:20.6px;color:var(--grey)}
.includes{left:618px;top:1222px;font-size:22px;color:var(--orange)}
.checks{left:618px;top:1268px;width:440px;list-style:none;font-size:13.5px;line-height:21px;color:var(--navy)}
.checks li{padding-left:17px;position:relative;margin-bottom:20px}
.checks li svg{position:absolute;left:0;top:5px}
.badge{left:475px;top:922px;width:107px;height:107px;background:var(--navy);border-radius:6px;color:var(--white);text-align:center;padding-top:18px}
.badge b{display:block;font-size:42px;font-weight:900;line-height:1}
.badge span{font-size:19px}

/* programs */
.prog-copy{font-size:15px;line-height:24px;color:var(--navy)}

/* footer */
.footer{left:0;top:2755px;width:1200px;height:441px;background:var(--navy);color:var(--white)}
.f-head{font-size:18px;font-weight:500}
.f-list{font-size:14px;line-height:28px}
.f-row{display:flex;gap:16px;font-size:14px;line-height:18px;margin-bottom:12px}
</style>
</head>
<body>

<!-- header -->
<div class="abs social" style="left:112px;top:24px"><span></span><span></span><span></span></div>
<div class="abs brand"><div class="mark"></div><div class="name">BRIGHTPATH AID<small>FOUNDATION</small></div></div>
<div class="btn" style="left:933px;top:17px;width:156px;height:46px;box-shadow:none">Donate Now</div>

<nav class="abs nav">
  <a class="active">Home</a><a>About us</a><i>|</i><a>Why Health?</a><i>|</i><a>Our Team</a><i>|</i><a>Eye Care Programs</a><i>|</i><a>Ear Care Programs</a><i>|</i><a>Contact Us</a>
</nav>

<!-- hero -->
<div class="abs hero" role="img" aria-label="Photo of a clinician performing an eye examination on an elderly patient, tinted orange to green"></div>
<div class="abs hero-copy">
  <p>Help bring</p>
  <p><span class="hl">Basic Health Care</span></p>
  <p>to every person on the</p>
</div>
<div class="abs planet">planet.</div>
<div class="btn" style="left:618px;top:516px;width:154px;height:46px;background:var(--green);box-shadow:none">Learn More</div>
<div class="abs slides"><span></span><span></span><span></span><span></span></div>

<div class="abs donate" style="left:112px;background:var(--orange)"><span class="lbl">Donate</span><div class="coin" style="background:var(--orange-deep)"><small>From</small><b>$10</b></div></div>
<div class="abs donate" style="left:438px;background:var(--lime)"><span class="lbl">Donate</span><div class="coin" style="background:var(--lime-deep)"><small>From</small><b>$20</b></div></div>
<div class="abs donate" style="left:763px;width:326px;background:var(--green)"><span class="lbl">Donate</span><div class="coin" style="background:var(--green-deep)"><small>From</small><b>$50</b></div></div>

<!-- about -->
<div class="abs" style="left:112px;top:891px;width:382px;height:635px;background:linear-gradient(160deg,#b7c83e,#9fb93a)" role="img" aria-label="Photo of an eye care worker with equipment, tinted lime green"></div>
<div class="abs" style="left:238px;top:1060px;width:345px;height:300px;background:linear-gradient(135deg,#cfd8e4,#b8a67a 60%,#d9b23a)" role="img" aria-label="Photo of community members gathered around a new water pump"></div>
<div class="abs badge"><b>70+</b><span>years</span></div>

<div class="abs kicker" style="left:618px;top:881px">About Us</div>
<div class="abs h-big" style="left:615px;top:910px;font-size:48px">BRIGHTPATH AID</div>
<div class="abs h-big" style="left:615px;top:970px;font-size:44px">FOUNDATION</div>
<p class="abs about-copy">Brightpath Aid Foundation is dedicated to improving and transforming the lives of people through enhanced vision and hearing health in the developing world. Our mission is to bridge the gap in access to essential eye and hearing care, ensuring that everyone, regardless of their circumstances, has the opportunity to see and hear clearly. With over 70 years of humanitarian aid across our members, we are passionate to provide innovative, sustainable, ethical and professional symbiotic solutions across multiple health programs.</p>
<div class="abs includes">This includes:</div>
<ul class="abs checks">
  <li><svg width="13" height="11" viewBox="0 0 13 11"><path d="M1 6l4 4 7-9" fill="none" stroke="#f0922d" stroke-width="2.2"/></svg>Providing eye care and treating preventable blindness</li>
  <li><svg width="13" height="11" viewBox="0 0 13 11"><path d="M1 6l4 4 7-9" fill="none" stroke="#f0922d" stroke-width="2.2"/></svg>Preventing and treating curable hearing loss and deafness</li>
  <li><svg width="13" height="11" viewBox="0 0 13 11"><path d="M1 6l4 4 7-9" fill="none" stroke="#f0922d" stroke-width="2.2"/></svg>Improving overall health through access to clean water, nutritious food and education</li>
  <li><svg width="13" height="11" viewBox="0 0 13 11"><path d="M1 6l4 4 7-9" fill="none" stroke="#f0922d" stroke-width="2.2"/></svg>Increase awareness in communities and education for preventing eye and ear diseases</li>
  <li><svg width="13" height="11" viewBox="0 0 13 11"><path d="M1 6l4 4 7-9" fill="none" stroke="#f0922d" stroke-width="2.2"/></svg>Strengthen health systems through clinics &amp; training of local doctors, nurses and other professionals</li>
</ul>
<div class="btn" style="left:618px;top:1543px;width:215px;height:46px">Learn More About Us</div>

<!-- eye care -->
<div class="abs" style="left:597px;top:1683px;width:603px;height:536px;background:linear-gradient(150deg,#f6c77e,#eaa24a 60%,#e09038)" role="img" aria-label="Photo of a nurse examining a patient's eyes in a clinic room, tinted orange"></div>
<div class="abs kicker" style="left:111px;top:1758px">Brightpath Aid</div>
<div class="abs h-big" style="left:108px;top:1792px;font-size:56px;line-height:54px">EYE CARE<br>PROGRAMS</div>
<p class="abs prog-copy" style="left:112px;top:1910px;width:465px">We all need our eyes to see and to complete our daily activities with ease. Imagine losing your eyesight, becoming dependent on family and friends for help and support to complete even the basic of activities. The loss of ability to take care of your family and work to make an honest living. This is the harsh reality for a lot of people in underprivileged communities.</p>
<div class="btn" style="left:112px;top:2096px;width:155px;height:46px">Learn More</div>

<!-- ear care -->
<div class="abs" style="left:0;top:2219px;width:597px;height:536px;background:linear-gradient(150deg,#5cc893,#3db872 55%,#7fd6a8)" role="img" aria-label="Photo of a clinician examining a patient's ear with an otoscope, tinted green"></div>
<div class="abs kicker" style="left:627px;top:2295px">Brightpath Aid</div>
<div class="abs h-big" style="left:624px;top:2328px;font-size:56px;line-height:54px">EAR CARE<br>PROGRAMS</div>
<p class="abs prog-copy" style="left:628px;top:2447px;width:465px">Hearing is a vital sense and gives us the ability to communicate with others in a way that none of our other senses can achieve. The loss of hearing can have a negative impact both on individuals and societies at large. It can lead to social isolation, the inability to work in the community and taking care of the family. Brightpath Aid Foundation Australia helps to establish mobile hearing clinics that include:</p>
<div class="btn" style="left:628px;top:2633px;width:156px;height:46px">Donate Now</div>

<!-- footer -->
<footer class="abs footer">
  <div class="abs" style="left:102px;top:100px;text-align:center;width:230px">
    <div style="width:56px;height:56px;border-radius:50%;background:var(--white);margin:0 auto 16px"></div>
    <div style="font-size:23px;font-weight:700;line-height:1;white-space:nowrap">BRIGHTPATH AID</div>
    <div style="font-size:16px;font-weight:700;letter-spacing:2px;margin-top:4px">FOUNDATION</div>
  </div>
  <div class="abs" style="left:166px;top:285px;display:flex;gap:16px;align-items:center">
    <span style="width:32px;height:32px;border-radius:50%;background:var(--orange)"></span>
    <span style="width:20px;height:20px;border-radius:50%;border:2px solid #fff"></span>
    <span style="width:20px;height:20px;border-radius:50%;border:2px solid #fff"></span>
  </div>

  <div class="abs f-head" style="left:406px;top:105px">Contact Us</div>
  <div class="abs" style="left:408px;top:140px;font-size:20px">Brightpath Aid Foundation</div>
  <div class="abs" style="left:408px;top:180px">
    <div class="f-row"><svg width="12" height="16" viewBox="0 0 12 16"><path d="M6 0a6 6 0 0 1 6 6c0 4-6 10-6 10S0 10 0 6a6 6 0 0 1 6-6z" fill="#fff"/><circle cx="6" cy="6" r="2.2" fill="#0b4862"/></svg><span>482 Harbour Row STE 12<br>&nbsp;Port Ellis, QLD 4870</span></div>
    <div class="f-row"><svg width="14" height="14" viewBox="0 0 14 14"><path d="M3 0l3 3-2 2c1 2 3 4 5 5l2-2 3 3-2 3C6 14 0 8 0 3z" fill="#fff"/></svg><span>+info@brightpathrelief.org.au</span></div>
    <div class="f-row"><svg width="14" height="12" viewBox="0 0 14 12"><rect x="1" y="1" width="12" height="10" fill="none" stroke="#fff" stroke-width="1.6"/><path d="M1 1l6 5 6-5" fill="none" stroke="#fff" stroke-width="1.6"/></svg><span>info@brightpathrelief.org.au</span></div>
  </div>

  <div class="abs f-head" style="left:726px;top:105px">Quick Links</div>
  <div class="abs f-list" style="left:728px;top:136px">Home<br>About Us<br>Why Health?<br>Our Team<br>Eye Care Programs<br>Ear Care Programs<br>Contact Us</div>

  <div class="abs" style="left:910px;top:107px;font-size:15px;font-weight:600">REGISTERED CHARITY</div>
  <div class="abs" style="left:937px;top:153px;width:124px;height:124px;border-radius:50%;background:var(--white);border:4px solid #5fc2a0"></div>

  <div class="abs" style="left:112px;top:361px;width:976px;height:1px;background:rgba(255,255,255,.25)"></div>
  <div class="abs" style="left:113px;top:392px;font-size:13.5px;opacity:.85">Brightpath Aid Foundation. © 2024. All Right Reserved</div>
  <div class="abs" style="left:888px;top:392px;font-size:13.5px;opacity:.85">Terms and Conditions &nbsp;| &nbsp;Privacy</div>
</footer>

</body>
</html>
```